Lift-Lark needs a design for a new mobile app

A new app - lift-lark.example, requires a design for its new app.

The app lets users add, create and share gym sessions. Sessions can be created, sets added and exercises chosen.

The app is currently functional on Android only (ios later), all that is required is a design for the app.

Some design assets are available (logo, colours, font), so the app should tie into these.

The design needs to be clean, simple and obvious, and all design assets will be required as part of this project.

One of the pages has % complete on the set - an icon to demonstrate this rather than a text based (eg 50%) would be great.

Screenshots will be available, along with the logos, colours and fonts.

Target Market(s)

Gym goers, all ages, male & female, fitness enthusiasts
Users of phones and tablets

Industry/Entity Type

Gym

Requirements
Must have
• Designs examples for each of the screens in the app, and an obvious selection of reusable elements (such as drop downs, radio buttons, buttons, calendar selectors, check boxes etc)
• Colours, logos and branding to fit into what is already available on the website.
• Usability and consistency are vital. Buttons should be in the same place (where possible).
• Design should help the user to complete the journey, and not get in the way.
• It should be a pleasure to use the app.
• Happy to have white space where appropriate.
• We use native elements where available.
Should not have
• Design features that waste space

```html
<!DOCTYPE html>
<html lang="en">
<head>
<meta charset="utf-8">
<title>Lift-Lark – Session</title>
<link rel="stylesheet" href="https://fonts.googleapis.com/css2?family=Montserrat:wght@400;500&display=swap">
<style>
  :root {
    --page-bg: #eef1f4;
    --status-blue: #0a84c9;
    --bar-blue: #1f93d0;
    --accent: #1ea1e6;
    --ring-track: #e3e3e3;
    --sub-bg: #f0f0f0;
    --divider: #e2e2e2;
    --title: #666666;
    --detail: #7a7a7a;
    --white: #ffffff;
  }
  * { box-sizing: border-box; margin: 0; padding: 0; }
  html, body { width: 1059px; height: 1200px; overflow: hidden; }
  body {
    background: var(--page-bg);
    font-family: "Montserrat", sans-serif;
    position: relative;
  }
  .screen {
    position: absolute; left: 212px; top: 35px;
    width: 635px; height: 1130px;
    background: var(--white);
    overflow: hidden;
  }
  .status-bar {
    height: 42px; background: var(--status-blue);
    display: flex; align-items: center; justify-content: flex-end;
    gap: 10px; padding-right: 12px; color: var(--white);
  }
  .status-time { font-size: 24px; font-weight: 500; margin-left: 8px; }
  .app-bar {
    height: 88px; background: var(--bar-blue);
    position: relative; color: var(--white);
  }
  .app-bar svg { position: absolute; }
  .app-title {
    position: absolute; left: 88px; top: 28px;
    font-size: 22px; font-weight: 500; letter-spacing: .3px;
  }
  .session-head {
    height: 54px; background: var(--sub-bg);
    position: relative;
  }
  .session-name {
    position: absolute; left: 13px; top: 16px;
    font-size: 18px; color: var(--detail);
  }
  .session-head svg { position: absolute; }
  .exercise {
    height: 153.5px; position: relative;
    border-bottom: 1px solid var(--divider);
  }
  .exercise-thumb {
    position: absolute; left: 13px; top: 15px;
    width: 131px; height: 123px;
    border: 1px solid #e6e6e6;
  }
  .thumb-trainer { background: linear-gradient(180deg, #f7f7f7 0%, #d9d9d9 100%); }
  .thumb-studio { background: linear-gradient(180deg, #f3ece6 0%, #b89aa6 100%); }
  .thumb-studio-plain { background: linear-gradient(180deg, #fbfbfb 0%, #e2d7cf 100%); }
  .exercise-name {
    position: absolute; left: 167px; top: 20px;
    font-size: 22px; font-weight: 500; color: var(--title); letter-spacing: .6px;
  }
  .exercise-sets {
    position: absolute; left: 167px; top: 55px;
    font-size: 19px; line-height: 27px; color: var(--detail); letter-spacing: .4px;
    list-style: none;
  }
  .progress {
    position: absolute; left: 533px; top: 32px;
    width: 90px; height: 90px;
  }
  .progress svg { position: absolute; left: 0; top: 0; }
  .progress-value {
    position: absolute; inset: 0;
    display: flex; align-items: center; justify-content: center;
    color: var(--accent); font-size: 18px;
  }
  .progress-value small { font-size: 11px; margin-top: 4px; }
</style>
</head>
<body>
<main class="screen">
  <div class="status-bar">
    <svg width="34" height="26" viewBox="0 0 34 26"><path d="M0 4 Q17 -6 34 4 L17 26 Z" fill="#fff"/></svg>
    <svg width="26" height="26" viewBox="0 0 26 26"><path d="M0 26 L26 0 L26 26 Z" fill="#fff"/></svg>
    <svg width="16" height="26" viewBox="0 0 16 26"><rect x="4" y="0" width="8" height="3" fill="#fff"/><rect x="0" y="3" width="16" height="23" rx="1" fill="#fff"/></svg>
    <span class="status-time">12:30</span>
  </div>

  <header class="app-bar">
    <svg style="left:14px;top:30px" width="32" height="26" viewBox="0 0 32 26" aria-label="Back"><path d="M30 13 H3 M13 2 L2 13 L13 24" stroke="#fff" stroke-width="2.5" fill="none"/></svg>
    <h1 class="app-title">18-May-2017</h1>
    <svg style="left:460px;top:31px" width="26" height="26" viewBox="0 0 26 26" aria-label="Info"><circle cx="13" cy="13" r="13" fill="#fff"/><rect x="11.3" y="11" width="3.4" height="9" fill="var(--bar-blue)"/><circle cx="13" cy="7.3" r="2" fill="var(--bar-blue)"/></svg>
    <svg style="left:541px;top:31px" width="24" height="26" viewBox="0 0 24 26" aria-label="Calendar"><rect x="1" y="4" width="22" height="21" fill="none" stroke="#fff" stroke-width="2"/><rect x="1" y="4" width="22" height="5" fill="#fff"/><rect x="5" y="0" width="2.5" height="6" fill="#fff"/><rect x="16.5" y="0" width="2.5" height="6" fill="#fff"/><g fill="#fff"><rect x="5" y="12" width="3" height="3"/><rect x="10.5" y="12" width="3" height="3"/><rect x="16" y="12" width="3" height="3"/><rect x="5" y="18" width="3" height="3"/><rect x="10.5" y="18" width="3" height="3"/><rect x="16" y="18" width="3" height="3"/></g></svg>
    <svg style="left:613px;top:31px" width="10" height="28" viewBox="0 0 10 28" aria-label="More"><circle cx="5" cy="4" r="3.3" fill="#fff"/><circle cx="5" cy="14" r="3.3" fill="#fff"/><circle cx="5" cy="24" r="3.3" fill="#fff"/></svg>
  </header>

  <div class="session-head">
    <span class="session-name">Test3</span>
    <svg style="left:534px;top:14px" width="24" height="24" viewBox="0 0 24 24" aria-label="Edit"><path d="M2 22 L3 16 L16 3 L21 8 L8 21 Z" fill="var(--accent)"/><path d="M17.5 1.5 L22.5 6.5" stroke="var(--accent)" stroke-width="3"/></svg>
    <svg style="left:602px;top:12px" width="20" height="26" viewBox="0 0 20 26" aria-label="Delete"><rect x="0" y="3" width="20" height="3" fill="var(--accent)"/><rect x="7" y="0" width="6" height="3" fill="var(--accent)"/><path d="M2 8 H18 V26 H2 Z" fill="var(--accent)"/><g fill="#f0f0f0"><rect x="5.5" y="11" width="2" height="12"/><rect x="9" y="11" width="2" height="12"/><rect x="12.5" y="11" width="2" height="12"/></g></svg>
  </div>

  <section class="exercise-list">
    <article class="exercise">
      <div class="exercise-thumb thumb-trainer" role="img" aria-label="Woman exercising on a cross trainer"></div>
      <h2 class="exercise-name">Cross Trainer</h2>
      <ul class="exercise-sets"><li>1000m - 10:00(High Effort)</li></ul>
      <div class="progress"><svg width="90" height="90"><circle cx="45" cy="45" r="42" fill="none" stroke="var(--accent)" stroke-width="5"/></svg><span class="progress-value">100<small>%</small></span></div>
    </article>

    <article class="exercise">
      <div class="exercise-thumb thumb-studio" role="img" aria-label="Woman doing dumbbell hammer curls"></div>
      <h2 class="exercise-name">Hammer Curls</h2>
      <ul class="exercise-sets"><li>5 x 22.0kg</li><li>5 x 22.0kg</li><li>5 x 22.0kg</li></ul>
      <div class="progress"><svg width="90" height="90"><circle cx="45" cy="45" r="42" fill="none" stroke="var(--ring-track)" stroke-width="5"/><circle cx="45" cy="45" r="42" fill="none" stroke="var(--accent)" stroke-width="5" stroke-dasharray="87 264" transform="rotate(-90 45 45)"/></svg><span class="progress-value">33<small>%</small></span></div>
    </article>

    <article class="exercise">
      <div class="exercise-thumb thumb-studio-plain" role="img" aria-label="Man holding an EZ curl bar"></div>
      <h2 class="exercise-name">Ez Bar Curl</h2>
      <ul class="exercise-sets"><li>6 x 33.0kg</li><li>6 x 33.0kg</li><li>6 x 33.0kg</li></ul>
      <div class="progress"><svg width="90" height="90"><circle cx="45" cy="45" r="42" fill="none" stroke="var(--ring-track)" stroke-width="5"/></svg><span class="progress-value">0<small>%</small></span></div>
    </article>

    <article class="exercise">
      <div class="exercise-thumb thumb-studio-plain" role="img" aria-label="Man doing dumbbell curls"></div>
      <h2 class="exercise-name">Dumbbell Curl</h2>
      <ul class="exercise-sets"><li>3 x 43.0kg</li><li>6 x 25.0kg</li></ul>
      <div class="progress"><svg width="90" height="90"><circle cx="45" cy="45" r="42" fill="none" stroke="var(--ring-track)" stroke-width="5"/><circle cx="45" cy="45" r="42" fill="none" stroke="var(--accent)" stroke-width="5" stroke-dasharray="132 264" transform="rotate(-90 45 45)"/></svg><span class="progress-value">50<small>%</small></span></div>
    </article>

    <article class="exercise">
      <div class="exercise-thumb thumb-studio-plain" role="img" aria-label="Woman doing curls with a resistance cable"></div>
      <h2 class="exercise-name">Cable Hammer Curls</h2>
      <div class="progress"><svg width="90" height="90"><circle cx="45" cy="45" r="42" fill="none" stroke="var(--ring-track)" stroke-width="5"/></svg><span class="progress-value">0<small>%</small></span></div>
    </article>

    <article class="exercise">
      <div class="exercise-thumb thumb-trainer" role="img" aria-label="Woman exercising on a cross trainer"></div>
      <h2 class="exercise-name">Hammer Curls</h2>
      <ul class="exercise-sets"><li>5 x 22.0kg</li><li>5 x 22.0kg</li><li>5 x 22.0kg</li></ul>
      <div class="progress"><svg width="90" height="90"><circle cx="45" cy="45" r="42" fill="none" stroke="var(--accent)" stroke-width="5"/></svg><span class="progress-value">100<small>%</small></span></div>
    </article>
  </section>
</main>
</body>
</html>
```